Grafik für Bibliothek
Zielgruppe
Anselm-Dreyhaupt-Bibliothek für Wandelstudien. Gemeinnütziger Verein, gegründet von Anselm Dreyhaupt (Freier Ehrenring Wessling). Im Interesse der Zivilgesellschaft. Schwerunkt Zukunftsdebatten.
Aufgabenstellung
Die Grafik steht am Ende einer Studie, die in einem Szenarioprozess einen 'Zukunftsraum' skizziert.
Vier Szenarios sind entstanden. Zwischen diesen spannt sich der Zukunftsraum auf. (Texte der Szeanrios anbei)
Die Szenarios basieren auf vielen Szenarienbündel, die geclustert als Punkte dargestellt sind. Diese vielen Punkte sind an sich nicht wichtig in der Darstellung, da sie zu einem Szenario verdichtet werden. Sie zeigen aber die Distanz zu den anderen Szenarien und einen methodischen Schritt an.
Diese unterscheiden sind an zwei Achsen. (Benennung anbei)
Die Szenarios sind unterschiedlich realistisch, das sollte grafisch sichtbar werden (in Vorlage - nicht gut - als Pfeile). (Bewertung in xx Punkten von 9 = sehr wahrscheinlich)
Die Grafik muss auf einer Powerpoint-Folie präsentierbar sein.
Logo der ADB

```html
<!DOCTYPE html>
<html lang="de">
<head>
<meta charset="utf-8">
<title>Salzburg 2040 – Zukunftsraum</title>
<link rel="stylesheet" href="https://fonts.googleapis.com/css2?family=Open+Sans:wght@400;600;700&display=swap">
<style>
  :root {
    --ink: #111111;
    --grid: #9a9a9a;
    --paper: #ffffff;
    --s1: #1d4f8b;
    --s2: #2e8fe3;
    --s3: #63d0ad;
    --s4: #8a3e12;
    --brand: #1f6a98;
  }
  html, body { margin: 0; padding: 0; overflow: hidden; background: var(--paper); }
  .canvas {
    position: relative; width: 1200px; height: 849px; overflow: hidden;
    background: var(--paper); color: var(--ink);
    font-family: "Open Sans", Arial, sans-serif;
  }
  .title {
    position: absolute; top: 66px; left: 0; width: 1200px; margin: 0;
    text-align: center; font-size: 30px; font-weight: 400; letter-spacing: 0.2px;
  }
  .chart { position: absolute; left: 0; top: 0; }
  .axis-label {
    position: absolute; font-size: 12.5px; font-weight: 700; line-height: 1.35; margin: 0;
  }
  .axis-top { left: 450px; width: 300px; top: 164px; text-align: center; }
  .axis-bottom { left: 450px; width: 300px; top: 655px; text-align: center; }
  .axis-left { left: 80px; width: 170px; top: 410px; text-align: center; }
  .axis-right { left: 930px; width: 160px; top: 410px; text-align: center; }
  .scenario {
    position: absolute; margin: 0; width: 172px; font-size: 12.5px; line-height: 1.4;
    text-align: justify; font-weight: 600;
  }
  .scenario b { font-weight: 700; }
  .scenario-1 { left: 64px; top: 200px; }
  .scenario-2 { left: 964px; top: 200px; width: 158px; }
  .scenario-3 { left: 964px; top: 568px; width: 158px; }
  .scenario-4 { left: 64px; top: 572px; }
  .probability { position: absolute; margin: 0; font-size: 14px; }
  .p1 { left: 308px; top: 288px; }
  .p2 { left: 812px; top: 316px; }
  .p3 { left: 724px; top: 478px; }
  .p4 { left: 308px; top: 566px; }
  .brand {
    position: absolute; left: 1000px; top: 728px; width: 180px;
    display: flex; align-items: flex-start; gap: 10px;
  }
  .brand-mark { flex: none; width: 22px; height: 22px; margin-top: 2px; background: var(--brand); }
  .brand-name {
    margin: 0; font-size: 14px; font-weight: 600; line-height: 1.3; color: var(--ink);
  }
</style>
</head>
<body>
<div class="canvas">
  <h1 class="title">Salzburg 2040 - Idee des Aufspannens des Zukunftsraumes</h1>

  <svg class="chart" width="1200" height="849" viewBox="0 0 1200 849" aria-hidden="true">
    <defs>
      <pattern id="grid-cell" x="266" y="200" width="10" height="10" patternUnits="userSpaceOnUse">
        <path d="M10 0 H0 V10" fill="none" stroke="var(--grid)" stroke-width="0.7"/>
      </pattern>
      <marker id="arrow" viewBox="0 0 10 10" refX="9" refY="5" markerWidth="9" markerHeight="9" orient="auto-start-reverse">
        <path d="M0 0 L10 5 L0 10 Z" fill="var(--ink)"/>
      </marker>
    </defs>
    <rect class="grid" x="266" y="200" width="667" height="448" fill="url(#grid-cell)" stroke="var(--grid)" stroke-width="0.8"/>
    <line class="axis-x" x1="270" y1="422" x2="929" y2="422" stroke="var(--ink)" stroke-width="1.6" marker-start="url(#arrow)" marker-end="url(#arrow)"/>
    <line class="axis-y" x1="600" y1="203" x2="600" y2="645" stroke="var(--ink)" stroke-width="1.6" marker-start="url(#arrow)" marker-end="url(#arrow)"/>

    <g class="cluster cluster-1" fill="var(--s1)">
      <circle cx="405" cy="271" r="14"/><circle cx="428" cy="259" r="14"/><circle cx="433" cy="264" r="14"/>
      <circle cx="445" cy="261" r="14"/><circle cx="450" cy="268" r="14"/><circle cx="470" cy="271" r="14"/>
      <circle cx="486" cy="251" r="14"/><circle cx="492" cy="268" r="14"/><circle cx="512" cy="268" r="14"/>
      <circle cx="522" cy="271" r="14"/><circle cx="563" cy="289" r="14"/><circle cx="396" cy="328" r="14"/>
      <circle cx="403" cy="332" r="14"/><circle cx="475" cy="331" r="14"/><circle cx="504" cy="328" r="14"/>
      <circle cx="526" cy="333" r="14"/><circle cx="405" cy="385" r="14"/><circle cx="410" cy="385" r="14"/>
      <circle cx="486" cy="395" r="14"/><circle cx="516" cy="390" r="14"/>
    </g>
    <g class="cluster cluster-2" fill="var(--s2)">
      <circle cx="740" cy="234" r="14"/><circle cx="751" cy="245" r="14"/><circle cx="760" cy="254" r="14"/>
      <circle cx="770" cy="269" r="14"/><circle cx="802" cy="237" r="14"/><circle cx="815" cy="251" r="14"/>
      <circle cx="795" cy="294" r="14"/><circle cx="804" cy="302" r="14"/><circle cx="764" cy="325" r="14"/>
    </g>
    <g class="cluster cluster-3" fill="var(--s3)">
      <circle cx="846" cy="403" r="14"/><circle cx="821" cy="443" r="14"/>
      <circle cx="836" cy="510" r="14"/><circle cx="824" cy="533" r="14"/>
    </g>
    <g class="cluster cluster-4" fill="var(--s4)">
      <circle cx="363" cy="445" r="14"/><circle cx="368" cy="456" r="14"/><circle cx="358" cy="463" r="14"/>
      <circle cx="370" cy="479" r="14"/><circle cx="365" cy="485" r="14"/><circle cx="403" cy="402" r="14"/>
      <circle cx="403" cy="415" r="14"/><circle cx="436" cy="450" r="14"/><circle cx="446" cy="463" r="14"/>
      <circle cx="450" cy="470" r="14"/><circle cx="484" cy="467" r="14"/><circle cx="486" cy="489" r="14"/>
      <circle cx="519" cy="460" r="14"/><circle cx="420" cy="513" r="14"/><circle cx="395" cy="532" r="14"/>
      <circle cx="388" cy="539" r="14"/><circle cx="406" cy="542" r="14"/><circle cx="428" cy="523" r="14"/>
      <circle cx="436" cy="534" r="14"/><circle cx="445" cy="547" r="14"/><circle cx="428" cy="567" r="14"/>
      <circle cx="507" cy="523" r="14"/><circle cx="519" cy="529" r="14"/><circle cx="527" cy="527" r="14"/>
      <circle cx="435" cy="601" r="14"/><circle cx="428" cy="610" r="14"/><circle cx="482" cy="598" r="14"/>
      <circle cx="490" cy="606" r="14"/><circle cx="480" cy="610" r="14"/><circle cx="546" cy="577" r="14"/>
      <circle cx="559" cy="567" r="14"/><circle cx="570" cy="559" r="14"/><circle cx="581" cy="556" r="14"/>
      <circle cx="589" cy="549" r="14"/><circle cx="542" cy="587" r="14"/>
    </g>
  </svg>

  <p class="axis-label axis-top">Weiterentwicklung<br>der bestehenden Konflikte</p>
  <p class="axis-label axis-bottom">Neue Konfliktlinien</p>
  <p class="axis-label axis-left">Moderater Fortschritt<br>des Klimawandels</p>
  <p class="axis-label axis-right">Stark beschleunigter<br>Klimawandel</p>

  <p class="scenario scenario-1"><b>Szenario 1:</b> Weiter so. Ein erfolgreiches Salzburg mit schwelenden Krisen</p>
  <p class="scenario scenario-2"><b>Szenario 2:</b> „Ellenbogen raus“ in der Krise. Ein Salzburg, das in der Klimakrise mit sich selbst ringt</p>
  <p class="scenario scenario-3"><b>Szenario 3:</b> Zusammen­stehen in der Krise. Ein Salzburg, das in der Krise zusammenrückt</p>
  <p class="scenario scenario-4"><b>Szenario 4:</b> Umbau mit Konflikten. Ein sich erneu­erndes Salzburg, das den Gegenwind spürt</p>

  <p class="probability p1">p = 60,0%</p>
  <p class="probability p2">p = 67,7%</p>
  <p class="probability p3">p = 46,6%</p>
  <p class="probability p4">p = 55,5%</p>

  <div class="brand">
    <span class="brand-mark" aria-hidden="true"></span>
    <p class="brand-name">Anselm-Dreyhaupt-Bibliothek für Wandelstudien</p>
  </div>
</div>
</body>
</html>
```